Landing Page Design for Cancer Article

We need to have relevant custom graphics and images incorporated with the text of the Google Doc. The Google Doc contains content for an article that informs users about Stomach Cancer. The article was written by a non-profit organization that promotes education and awareness about this disease. Their website address is www.halvermoot.org so you can see their current color theme and branding.

Basically, we're just looking to make the article look more polished. We don't want users coming to the article and just see a wall of text. We'd like graphics and images relevant to the content. Also the layout to make readability easier. Let me know if you have more questions.

https://files.quorvendex.com/document/d/7RkPaLmWxYtUeHnBcVsDoQiJgFzNmKwTe/edit?usp=sharing&ouid=904318276650192837461&rtpof=true&sd=true

```html
<!DOCTYPE html>
<html lang="en">
<head>
<meta charset="utf-8">
<title>About Stomach Cancer – Halvermoot Family Foundation</title>
<link href="https://fonts.googleapis.com/css2?family=Roboto+Slab:wght@400;500;600&family=Barlow:wght@400;500;600&display=swap" rel="stylesheet">
<style>
:root{
  --navy:#1b4f86;
  --navy-deep:#0c4a86;
  --blue:#2a6aa6;
  --sky:#dff1f8;
  --sky-soft:#eef8fb;
  --ink:#1f2a36;
  --white:#ffffff;
  --slab:"Roboto Slab",Georgia,serif;
  --sans:"Barlow",Arial,sans-serif;
}
*{margin:0;padding:0;box-sizing:border-box}
html,body{width:1200px;height:4354px;overflow:hidden;background:var(--white)}
body{position:relative;font-family:var(--sans);color:var(--ink)}
.abs{position:absolute}
.media{position:absolute}
.nowrap{white-space:nowrap}
.brand{display:flex;align-items:center;gap:14px;font-family:var(--slab);font-weight:500;color:var(--navy);line-height:1.05}
.brand-dot{width:46px;height:46px;border-radius:50%;background:var(--navy)}
.brand-name{font-size:26px;letter-spacing:.5px}
.brand-name span{display:block;font-size:16px;letter-spacing:3px}

/* hero */
.hero{position:absolute;left:0;top:0;width:1200px;height:745px;background:linear-gradient(180deg,#eaf7fb 0%,#f6fcfe 70%,#fff 100%);overflow:hidden}
.hero-title{position:absolute;left:98px;top:218px;font-family:var(--slab);font-weight:500;font-size:36px;line-height:1.18;color:var(--navy);white-space:nowrap}
.hero-intro{position:absolute;left:98px;top:378px;font-size:15.5px;line-height:1.6;color:var(--ink);white-space:nowrap}

/* section headings */
.section-title{position:absolute;left:98px;width:1004px;display:flex;align-items:center;gap:26px;font-family:var(--slab);font-weight:500;font-size:44px;color:var(--navy);white-space:nowrap}
.section-title::before,.section-title::after{content:"";flex:1;height:2px;background:var(--navy)}

/* causes */
.causes-kicker{position:absolute;left:549px;top:742px;width:553px;display:flex;align-items:center;gap:14px;font-family:var(--slab);font-size:27px;color:var(--ink)}
.causes-kicker::after{content:"";flex:1;height:2px;background:var(--navy)}
.causes-title{position:absolute;left:549px;top:776px;font-family:var(--slab);font-weight:600;font-size:57px;color:var(--navy);letter-spacing:.5px;white-space:nowrap}
.causes-body{position:absolute;left:549px;top:855px;width:580px;font-size:13.3px;line-height:1.42;color:var(--ink);white-space:nowrap}
.causes-body ul{list-style:none;margin-top:20px}
.causes-body li{font-weight:600}
.causes-body li::before{content:"• "}
.causes-body li.sub{font-weight:400}
.causes-body li.sub::before{content:"> "}
.causes-body li.sub.cont{padding-left:12px}
.causes-body li.sub.cont::before{content:""}

/* symptom panels */
.panel{position:absolute;background:linear-gradient(90deg,#dcf0f8,#eef9fb);border:3px solid var(--blue)}
.panel-early{left:-4px;top:1318px;width:1102px;height:280px;border-left:none;border-radius:0 140px 140px 0}
.panel-late{left:98px;top:1622px;width:1110px;height:280px;border-right:none;border-radius:140px 0 0 140px}
.panel-text{position:absolute;font-size:18.5px;line-height:1.35;color:#2b3a48;white-space:nowrap}
.ticks{list-style:none;margin-top:22px}
.ticks li{display:flex;align-items:center;gap:16px;color:var(--navy);font-weight:500;font-size:18.5px;height:25px}
.ticks svg{flex:none}

/* diagnosis */
.diag-intro{position:absolute;left:98px;top:2056px;width:1004px;font-size:15.5px;line-height:1.45}
.diag-lead{position:absolute;left:189px;top:2138px;font-size:15px;font-weight:600}
.diag-item{position:absolute;left:98px;width:1004px;display:flex;gap:37px}
.diag-icon{flex:none;width:54px;height:54px;border-radius:50%;background:var(--navy);display:flex;align-items:center;justify-content:center}
.diag-item p{font-size:14.5px;font-weight:600;line-height:1.45}
.diag-more{position:absolute;left:189px;top:2412px;font-size:15px}

/* treatments */
.treat{position:absolute;left:0;top:2493px;width:1200px;height:600px;background:linear-gradient(100deg,#1c5f97 0%,#3b80b4 45%,#79afd0 100%);overflow:hidden}
.treat-title{position:absolute;left:98px;top:36px;font-family:var(--slab);font-weight:400;font-size:46px;line-height:1.2;color:var(--white);white-space:nowrap}
.treat-copy{position:absolute;left:98px;top:182px;width:470px;font-size:14.3px;line-height:1.35;color:var(--white);text-align:justify;hyphens:auto}
.treat-copy p+p{margin-top:22px}
.treat-rule{position:absolute;left:592px;top:178px;width:3px;height:330px;background:rgba(255,255,255,.35)}
.treat-rule::after{content:"";position:absolute;left:0;top:140px;width:3px;height:30px;background:#fff}

/* survival */
.surv-intro{position:absolute;left:98px;top:3226px;width:1004px;font-size:15.5px;line-height:1.45}
.surv-intro p+p{margin-top:18px}
.stat{position:absolute;left:98px;width:936px;height:161px;background:linear-gradient(90deg,#cfe8f4,#eaf6fa)}
.stat p{position:absolute;left:48px;top:50%;transform:translateY(-50%);font-size:17px;font-weight:500;line-height:1.35;color:var(--navy);white-space:nowrap}
.stat-badge{position:absolute;left:978px;width:120px;height:120px;border-radius:50%;background:var(--navy-deep);color:#fff;font-weight:600;font-size:30px;display:flex;align-items:center;justify-content:center;box-shadow:0 0 0 5px #fff,0 0 0 7px var(--navy-deep)}

/* footer */
.footer{position:absolute;left:0;top:3940px;width:1200px;height:414px}
.footer-title{position:absolute;left:0;width:1200px;top:4150px;text-align:center;font-family:var(--slab);font-weight:400;font-size:44px;color:#fff}
.footer-text{position:absolute;left:98px;width:1004px;top:4218px;text-align:center;font-size:15.5px;line-height:1.45;color:#fff}
.footer-copy{position:absolute;left:0;width:1200px;top:4312px;text-align:center;font-size:11.5px;color:#fff;letter-spacing:.3px}
</style>
</head>
<body>

<!-- hero -->
<header class="hero">
  <div role="img" aria-label="Glowing red stomach held above an outstretched blue digital hand" class="media" style="left:560px;top:0;width:640px;height:700px;background:radial-gradient(circle at 52% 30%,#e0493f 0%,#e98a7f 18%,#bfe3f1 38%,#6aa9d8 55%,#e4f4fa 78%)"></div>
  <svg class="abs" style="left:0;top:560px" width="1200" height="190" viewBox="0 0 1200 190">
    <path d="M0 190 L0 150 C300 40 700 40 1200 40 L1200 190 Z" fill="#ffffff"/>
    <path d="M0 150 C300 40 700 40 1200 40" fill="none" stroke="#1f5d97" stroke-width="12"/>
    <path d="M0 120 C250 30 600 20 1000 0" fill="none" stroke="#2f7fc0" stroke-width="6"/>
  </svg>
  <div class="brand abs" style="left:98px;top:60px">
    <div class="brand-name">HALVERMOOT<span>FAMILY FOUNDATION</span></div>
    <div class="brand-dot"></div>
  </div>
  <h1 class="hero-title">About Stomach Cancer: Types,<br>Causes, Symptoms, Treatments,<br>Cures and Research</h1>
  <p class="hero-intro">Let’s go through the different causes and symptoms of stomach cancer.<br>Then, we’ll touch on some of the current ways to diagnose and treat<br>stomach cancer. Finally, we’ll discuss the survival rates and research<br>concerning stomach cancer. This guide is based on information from<br>the Calloway Oncology Institute (COI), an independent center<br>for cancer research.</p>
</header>

<!-- causes -->
<section>
  <div role="img" aria-label="Illustration of a stomach interior with cancer cells and a tumour" class="media" style="left:96px;top:760px;width:410px;height:410px;border-radius:50%;background:radial-gradient(circle at 45% 55%,#c85a78 0%,#6fb6d6 45%,#2a86b6 80%);box-shadow:8px 0 0 6px #8ec5de"></div>
  <div class="causes-kicker">Possible Causes of</div>
  <h2 class="causes-title">STOMACH CANCER</h2>
  <div class="causes-body">
    <p>Stomach cancer occurs for many reasons. For some people, genetics plays a significant<br>role. Here are some of the biggest risk factors associated with stomach cancer.</p>
    <ul>
      <li>Having any of the following medical conditions:</li>
      <li class="sub">Helicobacter pylori (H. pylori) infection of the stomach</li>
      <li class="sub">Chronic gastritis (inflammation of the stomach)</li>
      <li class="sub">Pernicious anemia</li>
      <li class="sub">Intestinal metaplasia (a condition in which the normal stomach</li>
      <li class="sub cont">lining is replaced with the cells that line the intestines)</li>
      <li class="sub">Gastric polyps</li>
      <li class="sub">Epstein-Barr virus infection</li>
      <li class="sub">Familial syndromes (including familial adenomatous polyposis)</li>
      <li>Eating a diet high in salted, smoked foods and low in fruits and vegetables.</li>
      <li>Eating foods that have not been prepared or stored properly.</li>
      <li>Being older or male.</li>
      <li>Smoking cigarettes.</li>
      <li>Having a mother, father, sister, or brother who has had stomach cancer.</li>
    </ul>
  </div>
</section>

<!-- symptoms -->
<section>
  <h2 class="section-title" style="top:1236px">Stomach Cancer Symptoms</h2>

  <div class="panel panel-early"></div>
  <div role="img" aria-label="Endoscope camera examining the inside of the stomach" class="media" style="left:130px;top:1346px;width:470px;height:226px;border:3px solid #fff;background:linear-gradient(120deg,#f3b7a6,#d2403a 50%,#f6c9a8)"></div>
  <div class="panel-text" style="left:634px;top:1355px">
    <p>In the early stages of stomach cancer, the<br>following signs and symptoms may occur:</p>
    <ul class="ticks">
      <li><svg width="18" height="18" viewBox="0 0 18 18"><circle cx="9" cy="9" r="9" fill="#1b4f86"/><path d="M5 9.3l2.7 2.6L13 6.5" fill="none" stroke="#fff" stroke-width="2.2"/></svg>Indigestion and stomach discomfort</li>
      <li><svg width="18" height="18" viewBox="0 0 18 18"><circle cx="9" cy="9" r="9" fill="#1b4f86"/><path d="M5 9.3l2.7 2.6L13 6.5" fill="none" stroke="#fff" stroke-width="2.2"/></svg>A bloated feeling after eating</li>
      <li><svg width="18" height="18" viewBox="0 0 18 18"><circle cx="9" cy="9" r="9" fill="#1b4f86"/><path d="M5 9.3l2.7 2.6L13 6.5" fill="none" stroke="#fff" stroke-width="2.2"/></svg>Mild nausea</li>
      <li><svg width="18" height="18" viewBox="0 0 18 18"><circle cx="9" cy="9" r="9" fill="#1b4f86"/><path d="M5 9.3l2.7 2.6L13 6.5" fill="none" stroke="#fff" stroke-width="2.2"/></svg>Loss of appetite</li>
      <li><svg width="18" height="18" viewBox="0 0 18 18"><circle cx="9" cy="9" r="9" fill="#1b4f86"/><path d="M5 9.3l2.7 2.6L13 6.5" fill="none" stroke="#fff" stroke-width="2.2"/></svg>Heartburn</li>
    </ul>
  </div>

  <div class="panel panel-late"></div>
  <div role="img" aria-label="Stomach tumour with magnified view of cancer cells" class="media" style="left:132px;top:1648px;width:465px;height:225px;background:linear-gradient(110deg,#e8d8cf,#9a5a40 45%,#f0b080 60%,#e7cfd2)"></div>
  <div class="panel-text" style="left:634px;top:1650px">
    <p>In more advanced stages of stomach cancer, the<br>following signs and symptoms may occur:</p>
    <ul class="ticks">
      <li><svg width="18" height="18" viewBox="0 0 18 18"><circle cx="9" cy="9" r="9" fill="#1b4f86"/><path d="M5 9.3l2.7 2.6L13 6.5" fill="none" stroke="#fff" stroke-width="2.2"/></svg>Blood in the stool</li>
      <li><svg width="18" height="18" viewBox="0 0 18 18"><circle cx="9" cy="9" r="9" fill="#1b4f86"/><path d="M5 9.3l2.7 2.6L13 6.5" fill="none" stroke="#fff" stroke-width="2.2"/></svg>Vomiting</li>
      <li><svg width="18" height="18" viewBox="0 0 18 18"><circle cx="9" cy="9" r="9" fill="#1b4f86"/><path d="M5 9.3l2.7 2.6L13 6.5" fill="none" stroke="#fff" stroke-width="2.2"/></svg>Weight loss for no known reason</li>
      <li><svg width="18" height="18" viewBox="0 0 18 18"><circle cx="9" cy="9" r="9" fill="#1b4f86"/><path d="M5 9.3l2.7 2.6L13 6.5" fill="none" stroke="#fff" stroke-width="2.2"/></svg>Stomach pain</li>
      <li><svg width="18" height="18" viewBox="0 0 18 18"><circle cx="9" cy="9" r="9" fill="#1b4f86"/><path d="M5 9.3l2.7 2.6L13 6.5" fill="none" stroke="#fff" stroke-width="2.2"/></svg>Jaundice (yellowing of eyes and skin)</li>
      <li><svg width="18" height="18" viewBox="0 0 18 18"><circle cx="9" cy="9" r="9" fill="#1b4f86"/><path d="M5 9.3l2.7 2.6L13 6.5" fill="none" stroke="#fff" stroke-width="2.2"/></svg>Ascites (build-up of fluid in the abdomen)</li>
      <li><svg width="18" height="18" viewBox="0 0 18 18"><circle cx="9" cy="9" r="9" fill="#1b4f86"/><path d="M5 9.3l2.7 2.6L13 6.5" fill="none" stroke="#fff" stroke-width="2.2"/></svg>Trouble swallowing</li>
    </ul>
  </div>
</section>

<!-- diagnosis -->
<section>
  <h2 class="section-title" style="top:1962px">Stomach Cancer Diagnosis</h2>
  <p class="diag-intro">If you or your doctor suspect you may have stomach cancer, make an appointment with a gastroenterologist, which is a doctor who specializes in the digestive system. During an appointment, they will ask you to provide them with stool and blood samples alongside a thorough physical examination.</p>
  <p class="diag-lead">They may also ask for imaging, including an:</p>
  <div class="diag-item" style="top:2170px">
    <div class="diag-icon" style="margin-top:6px"><svg width="26" height="26" viewBox="0 0 26 26"><path d="M8 3v8c0 6 4 8 8 8s6 3 4 5" fill="none" stroke="#fff" stroke-width="3" stroke-linecap="round"/></svg></div>
    <p>Upper gastrointestinal endoscopy where a doctor inserts a thin, lighted tube (an endoscope) into your mouth, down your esophagus, and into your stomach while you’re sedated or under anesthesia. The endoscope allows your doctor to look at the inner lining of the stomach wall. It can also be used to take a sample (biopsy) of any areas your doctor wants analyzed by a pathologist (a doctor who specializes in diagnosing disease).</p>
  </div>
  <div class="diag-item" style="top:2264px">
    <div class="diag-icon" style="margin-top:-4px"><svg width="24" height="26" viewBox="0 0 24 26"><rect x="3" y="2" width="18" height="22" rx="3" fill="none" stroke="#fff" stroke-width="2.5"/><path d="M8 9h8M8 13h8M8 17h8" stroke="#fff" stroke-width="2"/></svg></div>
    <p>Barium swallow X-rays or upper GI series. In this test you drink a liquid solution containing barium, a silver-white metal that shows up on an X-ray and helps doctors see a clear image of any potential abnormalities.</p>
  </div>
  <div class="diag-item" style="top:2332px">
    <div class="diag-icon" style="margin-top:-2px"><svg width="28" height="28" viewBox="0 0 28 28"><circle cx="14" cy="14" r="11" fill="none" stroke="#fff" stroke-width="3"/><circle cx="14" cy="14" r="4.5" fill="#fff"/></svg></div>
    <p>CT scan (CAT scan). A CT scan is a procedure that makes a series of detailed pictures of areas inside the body that are then linked to an X-ray machine.</p>
  </div>
  <p class="diag-more">Other tests will likely follow.</p>
</section>

<!-- treatments -->
<section class="treat">
  <div role="img" aria-label="Photo of a woman in a headscarf embracing a younger woman" class="media" style="left:610px;top:0;width:590px;height:600px;background:linear-gradient(180deg,#8fbfdc 0%,#c9a993 45%,#a9c9de 100%)"></div>
  <h2 class="treat-title">Stomach Cancer<br>Cure and Treatments</h2>
  <div class="treat-rule"></div>
  <div class="treat-copy">
    <p>In most cases, stomach cancers are only cured when diagnosed in the early stages. Stomach cancer has a five-year survival rate of 33.3 percent.</p>
    <p>Doctors will use some or all of the following treatments in an attempt to get your stomach cancer into remission including surgery, endoscopic mucosal resection, chemotherapy, radiation therapy, chemoradiation, targeted therapy and immunotherapy.</p>
    <p>Surgery is a common treatment for stomach cancer. The most common surgeries used include subtotal gastrectomy and total gastrectomy. The following procedures can be preformed if the tumor is blocking the stomach but the cancer cannot be removed by standard surgery: endoluminal stent placement, endoluminal laser therapy and gastrojejunostomy.</p>
    <p>Endoscopic mucosal resection is a procedure that uses an endoscope to remove any precancerous groths or early stage cancer from digestive tract lining without surgery.</p>
  </div>
</section>

<!-- survival -->
<section>
  <h2 class="section-title" style="top:3146px">Stomach Cancer Survival Rates</h2>
  <div class="surv-intro">
    <p>When people measure the survival rates of cancer, they primarily focus on the five-year survival rate. The five-year survival rate measures how many people with a certain type of cancer survived five years or more after diagnosis and the beginning of treatment.</p>
    <p>The Tracking, Registry and Case Evaluation (TRACE) program keeps track of cancer statistics in the United States. They also have a system to judge where cancer is in its growth cycle. There are three categories—localized, regional, and distant.</p>
  </div>
  <div class="stat" style="top:3372px"><p>Localized refers to cancer that only exists in the area where cancerous growth began. The<br>initial cancerous growth has not spread to any other part of the body. The five-year survival<br>rate for localized stomach cancer is</p></div>
  <div class="stat-badge" style="top:3394px">71.8%</div>
  <div class="stat" style="top:3549px"><p>Regional refers to cancer that has spread from its original location, but not to places far away.<br>In the case of stomach cancer, this could mean spreading to the esophagus or colon among<br>other locations. The five-year survival rate for regional stomach cancer is</p></div>
  <div class="stat-badge" style="top:3570px">32.9%</div>
  <div class="stat" style="top:3727px"><p>Distant refers to cancer that has spread to places far from the original location of the<br>cancerous growth. This could mean spreading to the lungs, brain, blood or any other part<br>of your body. The five-year survival rate for distant stomach cancer is</p></div>
  <div class="stat-badge" style="top:3748px">5.9%</div>
</section>

<!-- footer -->
<footer>
  <svg class="footer" width="1200" height="414" viewBox="0 0 1200 414">
    <path d="M0 40 C400 -10 800 -10 1200 40 L1200 414 L0 414 Z" fill="#2c73b0"/>
    <path d="M0 100 C400 30 800 30 1200 100 L1200 414 L0 414 Z" fill="#0c4a86"/>
  </svg>
  <div class="brand abs" style="left:474px;top:4022px;color:#fff">
    <div class="brand-name" style="color:#fff">HALVERMOOT<span>FAMILY FOUNDATION</span></div>
    <div class="brand-dot" style="background:#fff"></div>
  </div>
  <h2 class="footer-title">Final Word</h2>
  <p class="footer-text">Stomach cancer represents almost 1.4 percent of all new cancer cases in the US. Many factors influence the risk of getting stomach cancer. If you believe you are at risk of stomach cancer or exhibit any of the associated symptoms, contact your healthcare provide right away.</p>
  <p class="footer-copy">COPYRIGHT © 2022 HALVERMOOT FAMILY FOUNDATION | ALL RIGHT RESERVED</p>
</footer>

</body>
</html>
```